Plastic Surgeon Stationary Design

I Already have the logo. I Want and a clean, minimalist and elegant project. Please, I prefer Black, White and Gold color but you're free to try another ones. Business card,
Letterhead (A4 and Office), Recipes (Letter Pad) (A5), Envelop, Invoice, Computer Bill, Bill Book, Single A4 page size,
You Have to create at least the same materials I already own. I would like to a file to use in word to print letterheads and letter pad.
What I want that you make more changes are the envelopes that are to colorful and not elegant.
I'll not accept any design without my addresses as you can guide yourself with the models I provide.
Here are the addresses too:
"www.rubemtavorasilva.example" (website)
(My clinics' address)
"SÃO PAULO
Rua Lucas Bentim, 3180, Lucas Bentim Office, Cj 204
São Paulo - SP
(11) 90123-4567"
"BALNEÁRIO CAMBORIÚ
Rua Clemente Vilaça, 418, 7° andar
Edificio Torre Quaresma
Balneário Camboriú - SC
(047) 9012-3456"
Attention: Letterheads, Recipes, have to contain "CRM/SC 52.807 and CRM/SP 308.614" close to my name (Dr. Rubem Távora - Cirurgião Plástico), it is usually placed at the bottom.
Designers, attention!
During the process of creating bear in mind that the details of the logo, as the faces on the sides, are designed to be subtle. Highlight other such details affect the delicacy and elegance of the logo and visual identity.
When you are creating stationery, do not abuse the use of the logo, it should be used once or at most two times in each item.
Remember! Each stationery set must submit 3 models, one with the address "Balneario Camboriu", another with the address of "São Paulo" and the third containing both addresses.
The model letter envelope, folder type bag for letterhead and folder with inner pocket that provided a model did not please me because they are very flashy. Give preference to the use of white or black background.
PLEASE! Seek inspiration in the models contained in this link:
https://www.filecrate.example/sh/kq27zp41wcx905m/PlRtVuY_QX
In this link you can find my PAST Stationary Itens, so it can help you on your work
https://docuvault.example/7ZK3NB8QeT2LwYhR
Reason: Nobody presented anything useful.
Reason: still waiting some designers send their projects
Reason: Still Waiting Some Designs....
Target Market(s)
Mostly females with good economical condition. (Class A and AB)
Industry/Entity Type
Business
Requirements
Must have
- You have to provide 3 models of each paper, one with the address of São Paulo, another with the Balneario Camboriú address, and the third one with both addresses.

```html
<!DOCTYPE html>
<html lang="pt">
<head>
<meta charset="utf-8">
<title>Letterhead – Rubem Távora</title>
<link rel="stylesheet" href="https://fonts.googleapis.com/css2?family=Raleway:wght@300;400;500;600&display=swap">
<style>
  :root {
    --backdrop: #ececec;
    --paper: #ffffff;
    --ink: #3a3a3a;
    --ink-soft: #6a6a6a;
    --charcoal: #3b3b3b;
    --gold: #c9a908;
  }
  * { box-sizing: border-box; margin: 0; padding: 0; }
  html, body { width: 1200px; height: 795px; overflow: hidden; }
  body {
    background: var(--backdrop);
    font-family: "Raleway", sans-serif;
    color: var(--ink);
    position: relative;
  }
  .letterhead {
    position: absolute;
    left: 336px; top: 24px;
    width: 528px; height: 747px;
    background: var(--paper);
    box-shadow: 0 2px 10px rgba(0,0,0,.12);
  }
  .top-corner {
    position: absolute; top: 0; right: 0;
    width: 228px; height: 22px;
    border-top: 6px solid var(--charcoal);
    border-right: 6px solid var(--charcoal);
  }
  .bottom-corner {
    position: absolute; bottom: 0; right: 0;
    width: 235px; height: 190px;
    border-bottom: 8px solid var(--gold);
    border-right: 8px solid var(--gold);
  }
  .brand {
    position: absolute; left: 44px; top: 62px;
    display: flex; align-items: center; gap: 8px;
  }
  .brand-dot {
    width: 12px; height: 12px; border-radius: 50%;
    background: var(--gold);
  }
  .brand-name {
    font-size: 19px; font-weight: 600; color: var(--gold);
    letter-spacing: .2px;
  }
  .letter {
    position: absolute; left: 82px; top: 112px; width: 392px;
    font-size: 7.4px; line-height: 11px; font-weight: 400; color: var(--ink-soft);
  }
  .salutation { font-size: 11px; font-weight: 300; color: var(--ink); margin-bottom: 10px; }
  .letter p { margin-bottom: 11px; text-align: left; }
  .closing { margin-top: 16px; font-size: 8px; color: var(--ink); }
  .signature {
    display: block; width: 70px; height: 42px; margin: 8px 0 6px 40px;
    background: linear-gradient(90deg, rgba(60,60,60,.12), rgba(60,60,60,.04));
    border-radius: 4px;
  }
  .signatory { margin-left: 40px; }
  .signatory .name { font-size: 10px; color: var(--ink); font-weight: 400; }
  .signatory .role { font-size: 8px; color: var(--ink-soft); }
  .contacts {
    position: absolute; left: 150px; right: 30px; top: 612px;
    display: flex; gap: 20px;
    font-size: 5.6px; line-height: 8px; color: var(--ink-soft);
  }
  .contact { display: flex; gap: 4px; flex: 1; }
  .contact svg { flex: none; width: 8px; height: 10px; margin-top: 1px; }
  .contact strong { font-weight: 600; color: var(--ink); }
</style>
</head>
<body>
  <main class="letterhead">
    <div class="top-corner"></div>

    <header class="brand">
      <span class="brand-dot"></span>
      <span class="brand-name">Rubem Távora</span>
    </header>

    <article class="letter">
      <p class="salutation">Dear client</p>
      <p>Lorem ipsum dolor sit amet, consectetur adipisicing elit, sed do eiusmod tempor incididunt ut labore et dolore magna aliqua. Ut enim ad minim veniam, quis nostrud exercitation ullamco laboris nisi ut aliquip ex ea commodo consequat. Duis aute irure dolor in reprehenderit in voluptate velit esse cillum dolore eu fugiat nulla pariatur. Excepteur sint occaecat cupidatat non proident, sunt in culpa qui officia deserunt mollit anim id est laborum.</p>
      <p>Lorem ipsum dolor sit amet, consectetur adipisicing elit, sed do eiusmod tempor incididunt ut labore et dolore magna aliqua. Ut enim ad minim veniam, quis nostrud exercitation ullamco laboris nisi ut aliquip ex ea commodo consequat. Duis aute irure dolor in reprehenderit in voluptate velit esse cillum dolore eu fugiat nulla pariatur. Excepteur sint occaecat cupidatat non proident, sunt in culpa qui officia deserunt mollit anim id est laborum.</p>
      <p>Lorem ipsum dolor sit amet, consectetur adipisicing elit, sed do eiusmod tempor incididunt ut labore et dolore magna aliqua. Ut enim ad minim veniam, quis nostrud exercitation ullamco laboris nisi ut aliquip ex ea commodo consequat. Duis aute irure dolor in reprehenderit in voluptate velit esse cillum dolore eu fugiat nulla pariatur. Excepteur sint occaecat cupidatat non proident, sunt in culpa qui officia deserunt mollit anim id est laborum.</p>
      <p>Lorem ipsum dolor sit amet, consectetur adipisicing elit, sed do eiusmod tempor incididunt ut labore et dolore magna aliqua. Ut enim ad minim veniam, quis nostrud exercitation ullamco laboris nisi ut aliquip ex ea commodo consequat. Duis aute irure dolor in reprehenderit in voluptate velit esse cillum dolore eu fugiat nulla pariatur. Excepteur sint occaecat cupidatat non proident, sunt in culpa qui officia deserunt mollit anim id est laborum.</p>
      <p>Lorem ipsum dolor sit amet, consectetur adipisicing elit, sed do eiusmod tempor incididunt ut labore et dolore magna aliqua. Ut enim ad minim veniam, quis nostrud exercitation ullamco laboris nisi ut aliquip ex ea commodo consequat. Duis aute irure dolor in reprehenderit in voluptate velit esse cillum dolore eu fugiat nulla pariatur. Excepteur sint occaecat cupidatat non proident, sunt in culpa qui officia deserunt mollit anim id est laborum.</p>
      <p class="closing">Yours Sincerely,</p>
      <span class="signature" role="img" aria-label="Handwritten signature"></span>
      <div class="signatory">
        <div class="name">Rubem Távora</div>
        <div class="role">Cirurgião Plástico</div>
      </div>
    </article>

    <footer class="contacts">
      <div class="contact">
        <svg viewBox="0 0 8 10"><path d="M4 0a3.5 3.5 0 0 0-3.5 3.5C.5 6 4 10 4 10s3.5-4 3.5-6.5A3.5 3.5 0 0 0 4 0z" fill="var(--gold)"/><circle cx="4" cy="3.5" r="1.3" fill="#fff"/></svg>
        <div><strong>Dr. Rubem Távora</strong> - Cirurgião Plástico<br>CRM/SC 52.807<br>CRM/SP 308.614<br>www.rubemtavorasilva.example</div>
      </div>
      <div class="contact">
        <svg viewBox="0 0 8 10"><path d="M4 0a3.5 3.5 0 0 0-3.5 3.5C.5 6 4 10 4 10s3.5-4 3.5-6.5A3.5 3.5 0 0 0 4 0z" fill="var(--gold)"/><circle cx="4" cy="3.5" r="1.3" fill="#fff"/></svg>
        <div><strong>SÃO PAULO</strong><br>Rua Lucas Bentim, 3180, Lucas Bentim Office, Cj 204<br>São Paulo - SP<br>(11) 90123-4567</div>
      </div>
      <div class="contact">
        <svg viewBox="0 0 8 10"><path d="M4 0a3.5 3.5 0 0 0-3.5 3.5C.5 6 4 10 4 10s3.5-4 3.5-6.5A3.5 3.5 0 0 0 4 0z" fill="var(--gold)"/><circle cx="4" cy="3.5" r="1.3" fill="#fff"/></svg>
        <div><strong>BALNEÁRIO CAMBORIÚ</strong><br>Rua Clemente Vilaça, 418, 7° andar, Edificio Torre Quaresma<br>Balneário Camboriú - SC<br>(047) 9012-3456</div>
      </div>
    </footer>

    <div class="bottom-corner"></div>
  </main>
</body>
</html>
```